serious, thorough, light and simple - that's my advice and mediations

My business card should combine my logo (uploaded file) and my homepage (https://fellor-mediation.webnestsite.com).

Contact Information for Business Card

Name: Sabine Fellor di Vanti
Phone: 076 412 58 94
mail: sfellor@postkiv.ch
web: www.fellor-di-vanti.ch

```html
<!DOCTYPE html>
<html lang="de">
<head>
<meta charset="utf-8">
<title>Sabine Fellor di Vanti – Visitenkarte</title>
<link rel="stylesheet" href="https://fonts.googleapis.com/css2?family=Arimo:wght@400;700&display=swap">
<style>
  :root {
    --page: #e9e9e9;
    --card: #f3f3f3;
    --blue: #27367f;
    --green: #0a6836;
    --gold: #a6814b;
    --grey-text: #9a9a9a;
    --white: #ffffff;
  }
  html, body {
    margin: 0;
    padding: 0;
    width: 1200px;
    height: 1200px;
    overflow: hidden;
    background: var(--page);
    font-family: "Arimo", Arial, sans-serif;
  }
  .canvas {
    position: relative;
    width: 1200px;
    height: 1200px;
  }
  .card {
    position: absolute;
    left: 227px;
    width: 746px;
    height: 425px;
    overflow: hidden;
  }
  .card-front { top: 135px; background: var(--card); }
  .card-back {
    top: 638px;
    background: linear-gradient(to right, #263684 0%, #1a4f6a 45%, #076a36 100%);
  }

  .brand-name {
    position: absolute;
    margin: 0;
    font-weight: 700;
    white-space: nowrap;
    line-height: 1;
  }
  .card-front .brand-name {
    left: 34px;
    top: 62px;
    font-size: 32px;
    color: var(--gold);
  }
  .card-back .brand-name {
    left: 50%;
    top: 50%;
    transform: translate(-50%, -50%);
    font-size: 46px;
    color: var(--white);
  }

  .person-name {
    position: absolute;
    left: 34px;
    top: 293px;
    margin: 0;
    font-size: 22px;
    font-weight: 700;
    color: var(--blue);
  }
  .person-name .accent { color: var(--green); }

  .contact-row {
    position: absolute;
    left: 35px;
    top: 349px;
    display: flex;
    align-items: center;
    gap: 14px;
    font-size: 16px;
    color: var(--grey-text);
    white-space: nowrap;
  }
  .contact-item { display: flex; align-items: center; gap: 8px; }
  .contact-icon { width: 13px; height: 13px; flex: none; }

  .bands { position: absolute; left: 0; bottom: 0; }
</style>
</head>
<body>
<main class="canvas">

  <section class="card card-front" aria-label="Vorderseite">
    <p class="brand-name">Wege im Dialog</p>

    <h1 class="person-name">Sabine Fellor <span class="accent">di Vanti</span></h1>

    <div class="contact-row">
      <span class="contact-item">
        <svg class="contact-icon" viewBox="0 0 24 24" aria-hidden="true">
          <path fill="#0a6836" d="M6.6 10.8c1.4 2.8 3.8 5.1 6.6 6.6l2.2-2.2c.3-.3.7-.4 1-.2 1.1.4 2.3.6 3.6.6.6 0 1 .4 1 1V20c0 .6-.4 1-1 1C10.6 21 3 13.4 3 4c0-.6.4-1 1-1h3.5c.6 0 1 .4 1 1 0 1.3.2 2.5.6 3.6.1.3 0 .7-.2 1l-2.3 2.2z"/>
        </svg>
        076 412 58 94
      </span>
      <span class="contact-item">
        <svg class="contact-icon" viewBox="0 0 24 24" aria-hidden="true">
          <rect x="2" y="5" width="20" height="14" fill="none" stroke="#0a6836" stroke-width="2"/>
          <path d="M2 5l10 8 10-8M2 19l7-7M22 19l-7-7" fill="none" stroke="#0a6836" stroke-width="2"/>
        </svg>
        sfellor@postkiv.ch
      </span>
      <span class="contact-item">
        <svg class="contact-icon" viewBox="0 0 24 24" aria-hidden="true">
          <g fill="none" stroke="#0a6836" stroke-width="2">
            <circle cx="12" cy="12" r="10"/>
            <ellipse cx="12" cy="12" rx="4.5" ry="10"/>
            <path d="M2 12h20M4 7h16M4 17h16"/>
          </g>
        </svg>
        www.fellor-di-vanti.ch
      </span>
    </div>

    <svg class="bands" width="746" height="40" viewBox="0 0 746 40" aria-hidden="true">
      <polygon points="0,5 232,5 270,40 0,40" fill="var(--blue)"/>
      <polygon points="250,5 287,5 326,40 290,40" fill="var(--green)"/>
      <polygon points="314,17 746,17 746,40 340,40" fill="var(--gold)"/>
    </svg>
  </section>

  <section class="card card-back" aria-label="Rückseite">
    <p class="brand-name">Wege im Dialog</p>
  </section>

</main>
</body>
</html>
```